Web design for construction/ handyman company. We are a new company and trying to brand ourselves.

We have a logo with a character already in place and want a user friendly and simple site. I'm attaching our logo designs with our Crocodile character to get an idea of our logo. We want people to remember us and our site. The name we chose was so we could use a logo with a character. Our name is Pelican Builders LLC.

Target Market(s)

New clients

Industry/Entity Type

Contractor

Coding

Coded - Design and coding required

Number of Pages Required

4 page

Font styles to use
Sans Serif

Requirements
Must have
• About Us Page, What we do (not sure what to call this), Contact Us, Home Page. Would like the same colors as on our business card designs to be used on the website.
Nice to have
• We eventually want a project page to add photos of projects but thats not necessary now. Would be nice to use the crocodile theme, hammer or something similar somehow in the page names or clicks.

```html
<!DOCTYPE html>
<html lang="en">
<head>
<meta charset="utf-8">
<title>Pelican Builders LLC</title>
<link href="https://fonts.googleapis.com/css2?family=Open+Sans:wght@400;600;700;800&display=swap" rel="stylesheet">
<style>
:root{
  --blue:#1f6fb5;
  --blue-dark:#174f82;
  --navy:#1b3a5c;
  --green:#3a9a2b;
  --green-dark:#2c7a20;
  --ink:#2b2b2b;
  --muted:#777;
  --page:#eceff2;
  --white:#fff;
  --line:#d5dade;
}
*{box-sizing:border-box;margin:0;padding:0}
html,body{width:855px;height:1200px;overflow:hidden}
body{font-family:"Open Sans",Arial,sans-serif;background:var(--page);color:var(--ink);position:relative}
.site-header{position:absolute;left:0;top:0;width:855px;height:50px;background:var(--white)}
.brand{position:absolute;left:40px;top:8px;display:flex;align-items:center;gap:8px;font-weight:800;font-size:17px;color:var(--green-dark)}
.brand-mark{width:30px;height:30px;border-radius:50%;background:var(--green)}
.contact-pill{position:absolute;right:28px;top:5px;height:20px;display:flex;align-items:center;gap:14px;font-size:9px;color:var(--muted)}
.contact-pill .phone{background:var(--blue);color:var(--white);font-weight:700;font-size:10px;padding:3px 10px;border-radius:10px;display:flex;align-items:center;gap:5px}
.contact-pill .mail{display:flex;align-items:center;gap:4px}
.main-nav{position:absolute;right:28px;top:30px;display:flex;font-size:10px;font-weight:700}
.main-nav a{color:var(--ink);text-decoration:none;padding:2px 12px;border-left:1px solid var(--line)}
.main-nav a:first-child{border-left:none;color:var(--blue);border-bottom:2px solid var(--blue)}
.hero{position:absolute;left:0;top:50px;width:855px;height:400px;background:linear-gradient(160deg,#dfe6ec 0%,#b9c7d3 35%,#8f7a5f 70%,#c6b39a 100%)}
.hero-caption{position:absolute;left:172px;top:222px;width:520px;background:rgba(40,40,40,.72);color:var(--white);font-weight:700;font-size:16px;line-height:22px;text-align:center;padding:12px 20px}
.services{position:absolute;left:94px;top:456px;width:667px;height:246px;background:var(--white);box-shadow:0 1px 4px rgba(0,0,0,.15);padding:14px 16px}
.section-title{font-size:15px;font-weight:800;color:var(--ink);text-transform:uppercase;line-height:20px}
.section-title span{color:var(--blue)}
.service-grid{display:flex;gap:10px;margin-top:10px}
.service{width:151px}
.service-photo{height:106px;border:1px solid var(--line)}
.service h3{font-size:9.5px;font-weight:800;margin-top:8px;text-transform:uppercase}
.service p{font-size:8px;color:var(--muted);line-height:11px;margin-top:3px}
.welcome{position:absolute;left:94px;top:722px;width:667px;height:218px}
.welcome-title{position:absolute;left:0;top:0}
.mascot{position:absolute;left:14px;top:32px;width:84px;height:140px;border-radius:40px 40px 10px 10px;background:linear-gradient(180deg,#5fae3a,#2c7a20)}
.welcome-text{position:absolute;left:120px;top:32px;width:250px;font-size:8.5px;line-height:12.5px;color:var(--muted)}
.welcome-text p+p{margin-top:6px}
.btn{display:inline-block;background:var(--green);color:var(--white);font-size:9px;font-weight:700;padding:4px 10px;border-radius:2px}
.read-more{position:absolute;left:22px;top:184px}
.inquiry{position:absolute;left:412px;top:0;width:255px}
.inquiry form{margin-top:10px;display:flex;flex-direction:column;gap:6px}
.field{height:18px;border:1px solid var(--line);background:var(--white);font-size:8px;color:var(--muted);padding:3px 6px;line-height:11px}
.field.message{height:50px}
.inquiry .btn{align-self:flex-end;margin-top:2px}
.blog{position:absolute;left:0;top:945px;width:855px;height:210px;background:#dde2e6}
.blog-tab{position:absolute;left:362px;top:-2px;width:130px;height:24px;background:var(--green);color:var(--white);font-weight:800;font-size:13px;text-align:center;line-height:24px}
.blog-grid{position:absolute;left:108px;top:40px;display:flex;gap:32px}
.post{width:190px}
.post-photo{height:72px;border:1px solid var(--line)}
.post-meta{display:flex;gap:10px;font-size:8px;color:var(--blue);font-weight:600;margin-top:6px}
.post p{font-size:8px;line-height:11px;color:var(--muted);margin-top:4px}
.post .more{font-size:8.5px;font-weight:700;color:var(--green-dark);margin-top:3px}
.site-footer{position:absolute;left:0;top:1155px;width:855px;height:45px;background:var(--navy);color:#c9d3de}
.footer-links{position:absolute;left:108px;top:8px;display:flex;gap:16px;font-size:8.5px}
.copyright{position:absolute;left:108px;top:26px;font-size:7.5px}
.social{position:absolute;right:60px;top:11px;display:flex;gap:6px}
.social i{width:20px;height:20px;border-radius:50%;background:var(--white);display:block}
</style>
</head>
<body>
<header class="site-header">
  <div class="brand"><span class="brand-mark"></span>Pelican Builders LLC</div>
  <div class="contact-pill">
    <span class="mail"><svg width="10" height="8" viewBox="0 0 10 8"><rect x=".5" y=".5" width="9" height="7" fill="none" stroke="#1f6fb5"/><path d="M.5 .5 5 4.5 9.5 .5" fill="none" stroke="#1f6fb5"/></svg>info@pelicanbuilders.com</span>
    <span class="phone"><svg width="9" height="9" viewBox="0 0 10 10"><path d="M2 0 4 2.5 3 4a6 6 0 0 0 3 3l1.5-1L10 8 8.5 10C4 10 0 6 0 1.5Z" fill="#fff"/></svg>123-456-7890</span>
  </div>
  <nav class="main-nav"><a>HOME</a><a>ABOUT US</a><a>SERVICES</a><a>BLOG</a><a>CONTACT US</a></nav>
</header>

<section class="hero" role="img" aria-label="Contractors in hard hats with a couple inspecting a timber house frame">
  <div class="hero-caption">Lorem ipsum dolor sit amet consectetuer adipiscing elit sit amet consectetuer adipiscing elit</div>
</section>

<section class="services">
  <h2 class="section-title">Pelican Builders LLC <span>Services</span></h2>
  <div class="service-grid">
    <div class="service"><div class="service-photo" role="img" aria-label="Remodeled interior room" style="background:linear-gradient(135deg,#e8dfd2,#a88a68)"></div><h3>Interior Remodeling</h3><p>Lorem ipsum dolor sit amet, consectetuer adipiscing elit.</p></div>
    <div class="service"><div class="service-photo" role="img" aria-label="Painting and staining tools" style="background:linear-gradient(135deg,#c9d6e0,#5d7f99)"></div><h3>Painting &amp; Staining</h3><p>Lorem ipsum dolor sit amet, consectetuer adipiscing elit.</p></div>
    <div class="service"><div class="service-photo" role="img" aria-label="Hardwood flooring in a bright room" style="background:linear-gradient(135deg,#efe8dc,#b07a45)"></div><h3>Flooring &amp; Hardwood</h3><p>Lorem ipsum dolor sit amet, consectetuer adipiscing elit.</p></div>
    <div class="service"><div class="service-photo" role="img" aria-label="Freshly painted house exterior" style="background:linear-gradient(135deg,#a9c8e6,#6f8fa8)"></div><h3>Exterior Painting</h3><p>Lorem ipsum dolor sit amet, consectetuer adipiscing elit.</p></div>
  </div>
</section>

<section class="welcome">
  <h2 class="section-title welcome-title">Welcome to <span>Pelican Builders</span></h2>
  <div class="mascot" role="img" aria-label="Company mascot character in work clothes holding a hammer"></div>
  <div class="welcome-text">
    <p>Lorem ipsum dolor sit amet consectetuer adipiscing elit sed diam nonummy nibh euismod tincidunt ut laoreet dolore magna aliquam erat volutpat. Ut wisi enim ad minim veniam quis nostrud exerci tation ullamcorper suscipit lobortis nisl ut aliquip ex ea commodo consequat.</p>
    <p>Duis autem vel eum iriure dolor in hendrerit in vulputate velit esse molestie consequat, vel illum dolore eu feugiat nulla.</p>
  </div>
  <span class="btn read-more">Read More</span>
  <div class="inquiry">
    <h2 class="section-title">Quick Inquiry</h2>
    <form>
      <div class="field">Your Name</div>
      <div class="field">Phone</div>
      <div class="field">Email</div>
      <div class="field message">Message</div>
      <span class="btn">SUBMIT</span>
    </form>
  </div>
</section>

<section class="blog">
  <div class="blog-tab">BLOG POSTS</div>
  <div class="blog-grid">
    <article class="post"><div class="post-photo" role="img" aria-label="Workers in hard hats on site" style="background:linear-gradient(135deg,#f0c34a,#7d8a96)"></div><div class="post-meta"><span>20 May 2015</span><span>12:00 AM</span></div><p>Lorem ipsum dolor sit amet consectetuer adipiscing elit sed diam nonummy.</p><div class="more">Read More</div></article>
    <article class="post"><div class="post-photo" role="img" aria-label="Contractor meeting with clients" style="background:linear-gradient(135deg,#d9e2ea,#6d8193)"></div><div class="post-meta"><span>20 May 2015</span><span>12:00 AM</span></div><p>Lorem ipsum dolor sit amet consectetuer adipiscing elit sed diam nonummy.</p><div class="more">Read More</div></article>
    <article class="post"><div class="post-photo" role="img" aria-label="Builder working with tools" style="background:linear-gradient(135deg,#f2d36b,#3f6f9a)"></div><div class="post-meta"><span>20 May 2015</span><span>12:00 AM</span></div><p>Lorem ipsum dolor sit amet consectetuer adipiscing elit sed diam nonummy.</p><div class="more">Read More</div></article>
  </div>
</section>

<footer class="site-footer">
  <div class="footer-links"><span>Home</span><span>About Us</span><span>Services</span><span>Blog</span><span>Contact Us</span></div>
  <div class="copyright">Copyright © 2015 Pelican Builders. All Rights Reserved</div>
  <div class="social"><i></i><i></i><i></i></div>
</footer>
</body>
</html>
```